Pelican Crest landing page design

We need a landing page designed for an ecommerce website that sales fresh US domestic shrimp from the Gulf of Mexico and ships them direct to the consumer "From Our Shore To Your Door". For the landing page, we would like customers to be able to place an order and or inquire further about our product as well as links to social media. The company logo is attached

1 page

```html
<!DOCTYPE html>
<html lang="en">
<head>
<meta charset="utf-8">
<title>Pelican Crest — From Our Shore To Your Door</title>
<link rel="stylesheet" href="https://fonts.googleapis.com/css2?family=PT+Sans:wght@400;700&display=swap">
<style>
  :root {
    --coral: #d15c3f;
    --coral-panel: rgba(214, 92, 62, 0.86);
    --band-line: #5f5f5f;
    --button: #5c5c5c;
    --white: #ffffff;
    --ice-light: #f4f4f6;
    --ice-mid: #d9dadf;
    --shrimp: #e8cfc6;
    --shrimp-deep: #c9a39a;
  }
  * { margin: 0; padding: 0; box-sizing: border-box; }
  html, body { width: 1200px; height: 676px; overflow: hidden; }
  body { font-family: "PT Sans", sans-serif; background: var(--white); }
  .page { position: relative; width: 1200px; height: 676px; overflow: hidden; }

  .site-header {
    position: absolute; left: 0; top: 0; width: 1200px; height: 120px;
    background: var(--coral);
    border-bottom: 6px solid var(--band-line);
    display: flex; align-items: center; justify-content: center;
  }
  .brand { display: flex; align-items: center; gap: 14px; }
  .brand-mark {
    width: 70px; height: 70px; border-radius: 50%;
    border: 2px solid var(--band-line);
  }
  .brand-name {
    font-size: 34px; font-weight: 400; letter-spacing: 3px;
    color: var(--band-line); text-transform: uppercase;
  }

  .hero-photo {
    position: absolute; left: 0; top: 126px; width: 1200px; height: 550px;
    background:
      radial-gradient(ellipse 420px 300px at 600px 360px, var(--shrimp) 0%, var(--shrimp-deep) 45%, rgba(201,163,154,0) 80%),
      linear-gradient(180deg, var(--ice-light) 0%, var(--ice-mid) 100%);
  }

  .hero-title {
    position: absolute; left: 0; top: 170px; width: 1200px;
    text-align: center; color: var(--white);
    font-size: 38px; font-weight: 400; letter-spacing: 0.5px;
    text-shadow: 1px 2px 4px rgba(0,0,0,0.45);
  }

  .action-panel {
    position: absolute; left: 442px; top: 286px; width: 316px; height: 390px;
    background: var(--coral-panel);
  }
  .action-button {
    position: absolute; left: 38px; width: 238px; height: 52px;
    background: var(--button); color: var(--white);
    border-radius: 3px; text-decoration: none;
    display: flex; align-items: center; justify-content: center;
    font-size: 20px; letter-spacing: 1.5px; text-transform: uppercase;
    box-shadow: 0 1px 3px rgba(0,0,0,0.25);
  }
  .action-button.order { top: 38px; }
  .action-button.products { top: 114px; }

  .social-links {
    position: absolute; left: 0; bottom: 26px; width: 316px;
    display: flex; justify-content: center; gap: 13px; list-style: none;
  }
  .social-link {
    display: block; width: 36px; height: 36px; border-radius: 50%;
    background: var(--white); border: 3px solid var(--white);
    box-shadow: 0 1px 2px rgba(0,0,0,0.2);
  }
</style>
</head>
<body>
  <div class="page">
    <header class="site-header">
      <div class="brand">
        <span class="brand-mark"></span>
        <span class="brand-name">Pelican Crest</span>
      </div>
    </header>

    <div class="hero-photo" role="img" aria-label="Photo of fresh raw Gulf shrimp piled on crushed ice"></div>

    <h1 class="hero-title">From Our Shore To Your Door</h1>

    <section class="action-panel">
      <a class="action-button order" href="#order">Take Order</a>
      <a class="action-button products" href="#products">Our Products</a>
      <ul class="social-links">
        <li><a class="social-link" href="#" aria-label="Social profile 1"></a></li>
        <li><a class="social-link" href="#" aria-label="Social profile 2"></a></li>
        <li><a class="social-link" href="#" aria-label="Social profile 3"></a></li>
        <li><a class="social-link" href="#" aria-label="Social profile 4"></a></li>
      </ul>
    </section>
  </div>
</body>
</html>
```